Modern and Clean Web Re-Design Project

We have 2 companies in similar industries: Printing and Mail Preparation/Fulfillment. We prefer sites that are clean and easy to navigate.Our printing company, Harbourline Press Works' website, hpwdirect.example is outdated needs revamping. We have rebranded our logo and are looking for a new design that is clean, modern and geared to other corporations and business in the downtown Toronto area. Our mailing company, The Postwick Depot (thepostwickdepot.example) needs a website as well. This company is in the Direct Mail and letter shop business, which essentially is addressing/personalizing people's printed matter and preparing it for either the Canadian or US postal service. The Postwick Depot specializes in not-for-profit and corporate sectors.Please see our logos to get an idea of the colors and look we want. For all intensive purposes, the sites can look similar in design all we want is that each site has the appropriate corporate colors and is a bit different so they don't look identical as the two business run as separate corporations.The content of the website should be easily changed by our staff and we want it to be setup to optimized for SEO based on the keywords we want. We are looking for someone to work on this project immediately
Updates

Project Deadline Extended
Reason: Change of ideas

After doing some thinking, I would like the site to be more modern but the non flash sites that I have seen so far Im finding life-less and while I want something clean, not overly busy and corporate looking, I dont want the design to be bland looking.

Please design with the previous specs in mind but with a twist as mentioned above.

Thanks
Dorian

Target Market(s)

See above

Industry/Entity Type

Printing

Requirements
Must have
• Must match the design and style of each respective logoSee the attached impage of the front of our offices to have an idea of our lookWe must be able to edit the content ourselves without any fancy programs or tools.Must be SEO optimized
Nice to have
• An online order form that can be emailed to us for quotes.....perhaps a page with a bunch of fields that have drop down menus....
Should not have
• Should not be overly busy. I want it to be clean and simple but informative without being hard to navigate

```html
<!DOCTYPE html>
<html lang="en">
<head>
<meta charset="utf-8">
<title>Harbourline Press Works</title>
<link href="https://fonts.googleapis.com/css2?family=Dosis:wght@400;500;600&family=Vollkorn:wght@400&family=Arimo:wght@400;700&display=swap" rel="stylesheet">
<style>
:root{
  --orange:#f7a935;
  --orange-deep:#e8862a;
  --red:#ee4b2b;
  --rust:#c0531f;
  --brown:#9a7a5c;
  --ink:#2b2b2b;
  --muted:#7a716a;
  --paper:#ece6dd;
  --white:#ffffff;
  --dark:#2d2d2d;
}
*{margin:0;padding:0;box-sizing:border-box}
html,body{width:861px;height:1200px;overflow:hidden}
body{position:relative;background:var(--white);font-family:"Dosis",sans-serif;color:var(--ink)}
.abs{position:absolute}

/* header */
.brand{left:112px;top:30px;font:600 26px/1.1 "Dosis",sans-serif;color:var(--brown);width:230px;display:flex;align-items:center;gap:10px}
.brand-dot{width:20px;height:20px;border-radius:50%;background:var(--red);flex:none}
.phone{left:643px;top:18px;font:600 17px "Dosis",sans-serif;color:var(--brown)}
.mail{left:643px;top:37px;font:500 12px "Dosis",sans-serif;color:var(--muted)}
.nav{left:351px;top:68px;height:28px;display:flex;border:1px solid #ddd;border-radius:3px;background:linear-gradient(#fafafa,#e9e9e9)}
.nav a{font:500 13px/28px "Dosis",sans-serif;color:#6a6a6a;text-decoration:none;padding:0 11px;border-left:1px solid #d6d6d6}
.nav .home{width:32px;background:linear-gradient(#fbbd4c,var(--orange-deep));border:none;border-radius:3px 0 0 3px;display:flex;align-items:center;justify-content:center}

/* hero */
.hero{left:0;top:103px;width:861px;height:343px;border-top:2px solid var(--rust);border-bottom:2px solid var(--rust);
  background:linear-gradient(110deg,#e85a22 0%,#f39a2c 22%,#f4d23d 34%,#d2263b 48%,#f3b0c4 58%,#3d5fb8 70%,#7ab67d 84%,#c3c3c3 100%)}
.caption{height:30px;background:var(--orange);font:500 16px/30px "Arimo",sans-serif;color:#2a1a0a;padding-left:27px}
.c1{left:466px;top:217px;width:256px}
.c2{left:552px;top:251px;width:200px;padding-left:17px}
.c3{left:466px;top:284px;width:256px}
.c4{left:552px;top:318px;width:200px;padding-left:17px}
.slide-arrows{left:711px;top:350px;width:36px;height:19px;background:#333;display:flex}

/* content */
.main{left:0;top:446px;width:861px;height:573px;background:var(--paper)}
.photo{background:linear-gradient(135deg,#f6f6f6,#dedede);box-shadow:0 2px 6px rgba(0,0,0,.25);padding:12px}
.photo div{width:100%;height:100%}
.ph1{left:120px;top:498px;width:200px;height:210px;transform:rotate(-6deg)}
.ph1 div{background:linear-gradient(160deg,#3a4b57,#8a7b62 60%,#cfcfcf)}
.ph2{left:355px;top:785px;width:210px;height:200px;transform:rotate(12deg)}
.ph2 div{background:linear-gradient(135deg,#4a8bd0,#9bd05a 50%,#e05ab0)}
.clip{width:58px;height:30px;background:#c8202a}
.clip1{left:158px;top:495px;transform:rotate(-6deg)}
.clip2{left:470px;top:772px;transform:rotate(12deg)}

.heading{font:400 24px "Vollkorn",serif;color:var(--ink)}
.heading span{color:var(--orange-deep)}
.h1{left:369px;top:488px}
.h2{left:101px;top:772px}
.list{list-style:none;font:400 14px "Dosis",sans-serif;color:#6f6760}
.list li{height:23.3px;padding-left:18px;position:relative}
.list li::before{content:"";position:absolute;left:0;top:6px;border:4px solid transparent;border-left:6px solid #e8674a}
.l1{left:369px;top:531px}
.l2{left:102px;top:816px}
.more{font:700 9px "Arimo",sans-serif;color:#5a3a22}
.m1{left:369px;top:664px}
.m2{left:114px;top:970px}

/* quote form */
.quote{left:599px;top:482px;width:153px;height:323px;background:var(--orange)}
.quote-head{height:38px;background:var(--red);color:var(--white);font:600 19px/36px "Dosis",sans-serif;text-align:center;position:relative}
.quote-head::after{content:"";position:absolute;left:0;bottom:-8px;border-left:76.5px solid transparent;border-right:76.5px solid transparent;border-top:8px solid var(--red)}
.field{position:absolute;left:10px;width:133px;height:23px;background:linear-gradient(#fff,#fdf5e6);border-radius:2px;font:400 10px/23px "Arimo",sans-serif;color:#444;padding-left:6px}
.f-name{top:50px}.f-mail{top:82px}.f-phone{top:115px}
.f-comment{top:147px;height:68px;line-height:20px}
.code-label{position:absolute;left:10px;top:227px;font:400 9px/12px "Arimo",sans-serif;color:var(--white)}
.code{position:absolute;left:84px;top:227px;width:59px;height:24px;background:#eee;font:700 12px/24px "Arimo",monospace;text-align:center;color:#333}
.code-input{position:absolute;left:84px;top:259px;width:59px;height:22px;background:var(--white);border-radius:2px}
.submit{position:absolute;left:0;bottom:0;width:153px;height:32px;background:linear-gradient(#4a4a4a,#262626);color:var(--white);font:600 14px/32px "Dosis",sans-serif;text-align:center;letter-spacing:.5px}

/* footer */
.f-title{font:600 13px "Dosis",sans-serif;color:#8a5a30}
.ft1{left:100px;top:1036px}
.ft2{left:376px;top:1036px}
.f-text{left:100px;top:1055px;font:400 9px/11px "Arimo",sans-serif;color:var(--ink)}
.f-text p{margin-bottom:9px}
.socials{left:376px;top:1057px;display:flex;gap:6px}
.socials span{width:20px;height:20px;border-radius:2px}
.f-brand{left:600px;top:1058px;font:600 17px "Dosis",sans-serif;color:var(--brown);display:flex;align-items:center;gap:8px}
.bar{left:0;top:1138px;width:861px;height:62px;background:linear-gradient(90deg,#1d1d1d,#4a3a20 25%,#3a2a2a 50%,#2a3440 75%,#1d1d1d)}
.bar-links{left:0;top:1150px;width:861px;text-align:center;font:400 10px "Arimo",sans-serif;color:var(--white);word-spacing:1px}
.bar-links a{color:var(--white);text-decoration:none;margin:0 9px}
.copy{left:0;top:1166px;width:861px;text-align:center;font:400 8px "Arimo",sans-serif;color:#ddd}
</style>
</head>
<body>

<header>
  <div class="abs brand"><span class="brand-dot"></span>Harbourline Press Works</div>
  <div class="abs phone">416-555-0148</div>
  <div class="abs mail">info@hpwdirect.example</div>
  <nav class="abs nav">
    <a class="home" href="#" aria-label="Home"><svg width="12" height="11" viewBox="0 0 12 11"><path d="M6 0L0 5h2v6h3V7h2v4h3V5h2z" fill="#5a3312"/></svg></a>
    <a href="#">What are we</a>
    <a href="#">What do we do</a>
    <a href="#">Email a file</a>
    <a href="#">Contact us</a>
  </nav>
</header>

<section class="abs hero" role="img" aria-label="Close-up photo of a fanned colour swatch guide"></section>
<div class="abs caption c1">Neque porro quisquam est qui</div>
<div class="abs caption c2">consectetur, adipisci velit</div>
<div class="abs caption c3">Neque porro quisquam est qui</div>
<div class="abs caption c4">consectetur, adipisci velit</div>
<div class="abs slide-arrows">
  <svg width="36" height="19" viewBox="0 0 36 19"><path d="M12 4l-5 5.5 5 5.5M24 4l5 5.5-5 5.5" stroke="#fff" stroke-width="2" fill="none"/><path d="M18 2v15" stroke="#666"/></svg>
</div>

<main class="abs main"></main>

<div class="abs photo ph1"><div role="img" aria-label="Photo of two print shop workers in hard hats"></div></div>
<div class="abs clip clip1"></div>
<h2 class="abs heading h1"><span>What</span> are we</h2>
<ul class="abs list l1">
  <li>Mission Statement</li><li>Hours of Operation</li><li>Where are we located</li><li>Pick up and delivery</li><li>Grow your business</li>
</ul>
<a class="abs more m1">Read More ›</a>

<h2 class="abs heading h2"><span>What</span> do we do</h2>
<ul class="abs list l2">
  <li>Digital printing</li><li>Commercial printing</li><li>Legal services</li><li>Mailing house</li><li>Computer services</li><li>Free pick up and delivery</li>
</ul>
<a class="abs more m2">Read More ›</a>
<div class="abs photo ph2"><div role="img" aria-label="Photo collage of colourful printed images"></div></div>
<div class="abs clip clip2"></div>

<form class="abs quote">
  <div class="quote-head">Get a Quote</div>
  <div class="field f-name">Name</div>
  <div class="field f-mail">Email-Id</div>
  <div class="field f-phone">Phone no.</div>
  <div class="field f-comment">Comment</div>
  <div class="code-label">Enter<br>the code</div>
  <div class="code">b52c46</div>
  <div class="code-input"></div>
  <div class="submit">SUBMIT</div>
</form>

<footer>
  <div class="abs f-title ft1">Contact</div>
  <div class="abs f-text">
    <p>84 Carrow Street West<br>Toronto, Ontario, M5V 0A0</p>
    <p>E-mail: dorian@hpwdirect.example</p>
    <p>PC &amp; Mac Files E-mail: mac@hpwdirect.example</p>
  </div>
  <div class="abs f-title ft2">Follow us with</div>
  <div class="abs socials">
    <span style="background:#7b1e8c"></span><span style="background:#f08a1c"></span><span style="background:#3b5998"></span><span style="background:#4fb8e8"></span>
  </div>
  <div class="abs f-brand"><span class="brand-dot"></span>Harbourline Press Works</div>
  <div class="abs bar"></div>
  <div class="abs bar-links"><a>Home</a><a>What are we</a><a>What do we do</a><a>Email a file</a><a>Contact us</a></div>
  <div class="abs copy">Copyright © 2013 Harbourline Press Works. All Rights Reserved.</div>
</footer>

</body>
</html>
```